Copperleaf Motorized Shade Business Card

Hello, we've had our logo made. Now we are looking for a clean and cool looking business card. One side can just be the logo with any design elements that might look good with it. The other side will be Name, Phone Number and Email. There will not be an address on the card.

```html
<!DOCTYPE html>
<html lang="en">
<head>
<meta charset="UTF-8">
<title>Copperleaf Motorized Shade Business Card</title>
<link rel="stylesheet" href="https://fonts.googleapis.com/css2?family=Oswald:wght@600&family=Quicksand:wght@400&display=swap">
<style>
  :root {
    --backdrop: #262626;
    --navy: #0d3f7e;
    --navy-deep: #0a3570;
    --sun: #fcc314;
    --paper: #ffffff;
    --ink-grey: #4a4a4a;
  }
  * { margin: 0; padding: 0; box-sizing: border-box; }
  html, body {
    width: 1200px;
    height: 900px;
    overflow: hidden;
    background: var(--backdrop);
  }
  .sheet {
    position: relative;
    width: 1200px;
    height: 900px;
  }
  .card {
    position: absolute;
    left: 250px;
    width: 700px;
    height: 400px;
    overflow: hidden;
  }
  .card-front {
    top: 40px;
    background: var(--navy);
  }
  .card-front .brand-name {
    position: absolute;
    left: 190px;
    bottom: 80px;
    font-family: "Oswald", sans-serif;
    font-weight: 600;
    font-size: 34px;
    letter-spacing: 1px;
    color: var(--paper);
    text-transform: uppercase;
  }
  .card-back {
    top: 470px;
    background: var(--paper);
  }
  .sun-panel {
    position: absolute;
    left: 0;
    top: 70px;
    width: 300px;
    height: 330px;
    background: var(--sun);
  }
  .holder-name {
    position: absolute;
    left: 36px;
    top: 262px;
    font-family: "Oswald", sans-serif;
    font-weight: 600;
    font-size: 40px;
    color: var(--navy-deep);
    text-transform: uppercase;
    letter-spacing: 0.5px;
  }
  .card-back .brand-name {
    position: absolute;
    right: 40px;
    top: 120px;
    width: 340px;
    text-align: right;
    font-family: "Oswald", sans-serif;
    font-weight: 600;
    font-size: 40px;
    line-height: 1.1;
    color: var(--navy-deep);
    text-transform: uppercase;
  }
  .contact {
    position: absolute;
    right: 40px;
    bottom: 60px;
    text-align: right;
    font-family: "Quicksand", sans-serif;
    font-weight: 400;
    color: var(--ink-grey);
  }
  .contact .phone { font-size: 30px; line-height: 1.2; }
  .contact .email { font-size: 22px; line-height: 1.3; }
</style>
</head>
<body>
  <main class="sheet">
    <section class="card card-front">
      <p class="brand-name">Copperleaf Motorized Shade</p>
    </section>

    <section class="card card-back">
      <div class="sun-panel" role="img" aria-label="Large yellow setting-sun graphic with horizontal stripes"></div>
      <p class="holder-name">Marcus Hale</p>
      <p class="brand-name">Copperleaf Motorized Shade</p>
      <div class="contact">
        <p class="phone">555. 214. 0193</p>
        <p class="email">hello@copperleafshade.com</p>
      </div>
    </section>
  </main>
</body>
</html>
```